Reservation Confirmation Template

Update:

- added more clarification about what content needs to be included.
- changed project to guaranteed status
- Added $50 to first place

We are a vacation rental company in need of an email template to be used for reservation confirmations. This will be turned into HTML which will be uploaded to our property management system which will use merge fields to populate the actual content. for the purposes of this project, you can use dummy text.

It should be branded and include a section thanking the guest for booking, reservation details, property details, policy details, checkin instructions, etc.

I tried to include a screenshot of our website but it won't allow me to upload it because the dimensions are too large. Please check out our website to use as guidance for look and feel. https://loftquelle.com

There should be a place holder for a property image. There should also be a place holder at the bottom for additional services.

Visit our website for branding. I have digital assets such as icons, logos, etc if you require additional branded images or graphics, please message me. I can give you access to our Brindlework drive.

See the brand guidelines for our colors and fonts.

Target Market(s)

Confirmed vacation rental guests

Industry/Entity Type

Hotel

Font styles to use
Other font styles liked:
• See brand guidelines

Requirements
Must have
• If you think about booking a hotel and receiving a confirmation, that is what we are looking for. The difference for us is that we are a vacation rental company so there are many more details in our confirmations versus a hotel. As such, the following sections need to be included:

Guest Details
- Name
- Phone Number
- Email Address
- # Adults
- # Kids

Property Details
- Image placeholder
- Property Name
- Property Address

- Access Instructions (door code)
- Check in Instructions
- Checkout Instructions
- Parking Details
- Wifi Instructions
- House Rules

Getting Help
- Phone Number
- Email
- Hours
- Emergency Contact

Additional Services
- 3 placeholders split into thirds 100% width at the bottom

In my mind, each section would have a header with either some kind of icon or small graphic. We have already paid to have custom icons created. I will include those in the upload section.
Nice to have
• Everything is mentioned in the project description
Should not have

```html
<!DOCTYPE html>
<html lang="en">
<head>
<meta charset="utf-8">
<title>Loftquelle – Reservation Confirmation</title>
<link href="https://fonts.googleapis.com/css2?family=Montserrat:wght@400;500;600;700;800;900&family=Crimson+Text:ital@1&display=swap" rel="stylesheet">
<style>
:root{
  --mint:#b4fbd6;
  --mint-soft:#d8fde9;
  --orange:#f58a61;
  --orange-light:#ffd9c8;
  --ink:#1c1c1c;
  --page:#f3f3f3;
  --paper:#ffffff;
  --policy:#efefef;
  --line:#e6e6e6;
}
*{box-sizing:border-box;margin:0;padding:0}
html,body{width:1200px;height:3992px;overflow:hidden;background:var(--page)}
body{font-family:"Montserrat",Arial,sans-serif;color:var(--ink);position:relative}
.email{position:absolute;left:248px;top:0;width:704px;height:3992px;background:var(--paper);overflow:hidden}
.block{position:absolute;left:0;width:704px}

.brand{top:170px;text-align:center}
.brand-name{font-size:48px;font-weight:800;line-height:1}
.brand-tag{font-size:17px;font-weight:500;margin-top:8px}

.hero-band{top:352px;height:468px;background:var(--mint)}
.hero-title{top:372px;text-align:center;font-size:38px;font-weight:900;letter-spacing:.5px}
.hero-photo{position:absolute;left:40px;width:624px;top:448px;height:344px;background:linear-gradient(180deg,#b9c7d6 0%,#9aa9b4 45%,#6f7c70 70%,#5c6b5e 100%);box-shadow:0 6px 14px rgba(0,0,0,.18)}
.confirmed{top:836px;text-align:center;color:var(--orange);font-size:30px;font-weight:700}
.intro{top:880px;left:40px;width:624px;text-align:center;font-family:"Crimson Text",Georgia,serif;font-style:italic;font-size:19px;line-height:26px}

.section-bar{position:absolute;left:40px;width:624px;height:52px;background:var(--mint);display:flex;align-items:center;justify-content:center;font-size:22px;font-weight:800;letter-spacing:.5px}
.art{position:absolute;left:40px;width:232px;background:linear-gradient(180deg,#f7d2c1,#f4a78a 60%,#2f4a8a);border-radius:6px}
.details{position:absolute;left:312px;width:352px}
.detail-row{display:flex;align-items:center;height:64px;font-size:19px;border-bottom:1px solid var(--line)}
.detail-row.last{border-bottom:none}
.ic{width:32px;height:32px;flex:none;margin-right:16px}
.counts{gap:50px}
.counts span{display:flex;align-items:center}

.res-art{background:linear-gradient(180deg,#d6ecff,#6fa6e3 55%,#f58a61)}
.res-item{position:absolute;left:312px;font-size:19px;line-height:28px}
.res-item strong{display:block;font-weight:700}

.amenities{top:1832px;display:flex;justify-content:center;gap:70px}
.amenity{text-align:center;width:160px}
.amenity svg{width:88px;height:88px}
.amenity p{font-size:21px;font-weight:700;margin-top:22px}

.property-band{top:2040px;height:540px;background:var(--mint)}
.property-title{top:2060px;text-align:center;font-size:22px;font-weight:800}
.property-photo{position:absolute;left:40px;width:624px;top:2116px;height:344px;background:linear-gradient(135deg,#f4f1ec 0%,#dcd6cc 50%,#8d8a80 100%);box-shadow:0 5px 12px rgba(0,0,0,.15)}
.property-name{top:2490px;text-align:center;font-size:32px;font-weight:700}
.property-meta{top:2540px;text-align:center;font-size:19px;font-weight:500}

.actions{top:2652px;display:flex;justify-content:center;gap:60px}
.btn{width:220px;height:64px;display:flex;align-items:center;justify-content:center;font-size:24px;font-weight:800;letter-spacing:1px}
.btn-modify{background:var(--mint)}
.btn-cancel{border:3px solid var(--mint);background:var(--paper)}

.policy{top:2772px;height:432px;background:var(--policy);padding:36px 44px 0;text-align:center}
.policy h2{font-size:24px;font-weight:800}
.policy p{font-family:"Crimson Text",Georgia,serif;font-style:italic;font-size:18px;line-height:24px;margin-top:22px}
.policy p + p{margin-top:26px}
.btn-read{display:inline-flex;margin-top:30px;border:2px solid var(--orange);padding:14px 26px;font-size:23px;font-weight:800;background:var(--paper)}

.help{top:3260px;height:300px}
.help-info{position:absolute;left:40px;top:0;width:380px}
.help h2{font-size:23px;font-weight:800}
.help-rule{width:96px;height:3px;background:var(--orange);margin:10px 0 14px}
.help .detail-row{border:none;height:66px;font-size:19px}
.emergency{position:absolute;left:430px;top:-12px;width:240px;text-align:center}
.emergency-art{width:130px;height:232px;margin:0 auto;background:linear-gradient(180deg,#c86a34 0%,#f3d3c4 40%,#4aa6d6 75%,#2e5da8 100%);border-radius:8px}
.emergency p{font-size:18px;margin-top:10px}
.emergency strong{display:block;color:var(--orange);font-size:19px;font-weight:700;margin-top:4px}

.services{top:3572px;height:208px;background:var(--orange);color:#fff;text-align:center;padding-top:38px}
.services h2{font-size:26px;font-weight:700;letter-spacing:1px}
.services-rule{width:96px;height:2px;background:#fff;margin:12px auto 18px;opacity:.8}
.services p{font-size:18px;color:var(--orange-light)}

.footer{top:3780px;height:212px;display:flex;align-items:center;justify-content:center;gap:20px;font-size:20px;font-weight:500}
.social{width:36px;height:36px;border:3px solid var(--ink);border-radius:50%}
</style>
</head>
<body>
<main class="email">
  <header class="block brand">
    <div class="brand-name">Loftquelle</div>
    <div class="brand-tag">vacation rentals reinvented.</div>
  </header>

  <div class="block hero-band"></div>
  <h1 class="block hero-title">THANK YOU FOR BOOKING</h1>
  <div class="hero-photo" role="img" aria-label="Rooftop terrace with lounge seating overlooking a city skyline"></div>
  <p class="block confirmed">Your reservation is confirmed</p>
  <p class="block intro">If you think about booking a hotel and receiving a confirmation, that is what we are looking for. The difference for us is that we are a vacation rental company so there are many more details in our confirmations versus a hotel.</p>

  <h2 class="section-bar" style="top:1008px">GUEST DETAILS</h2>
  <div class="art" style="top:1084px;height:276px" role="img" aria-label="Illustration of a traveller pulling a suitcase"></div>
  <div class="details" style="top:1092px">
    <div class="detail-row"><svg class="ic" viewBox="0 0 34 34"><circle cx="17" cy="17" r="15" fill="none" stroke="var(--orange)" stroke-width="2.5"/><circle cx="17" cy="13" r="4" fill="var(--orange)"/><path d="M10 24c1-4 4-6 7-6s6 2 7 6" fill="var(--orange)"/></svg>Dana Whitfield</div>
    <div class="detail-row"><svg class="ic" viewBox="0 0 34 34"><circle cx="17" cy="17" r="15" fill="none" stroke="var(--orange)" stroke-width="2.5"/><path d="M12 10l3 0 1 4-2 1c1 2 2 3 4 4l1-2 4 1 0 3c-6 0-11-5-11-11z" fill="var(--orange)"/></svg>555-014-2290</div>
    <div class="detail-row"><svg class="ic" viewBox="0 0 34 34"><circle cx="17" cy="17" r="15" fill="none" stroke="var(--orange)" stroke-width="2.5"/><rect x="10" y="12" width="14" height="10" fill="none" stroke="var(--orange)" stroke-width="2"/><path d="M10 12l7 6 7-6" fill="none" stroke="var(--orange)" stroke-width="2"/></svg>dana@inboxly.com</div>
    <div class="detail-row counts last">
      <span><svg class="ic" viewBox="0 0 34 34"><circle cx="17" cy="17" r="15" fill="none" stroke="var(--orange)" stroke-width="2.5"/><circle cx="17" cy="13" r="4" fill="var(--orange)"/><path d="M10 24c1-4 4-6 7-6s6 2 7 6" fill="var(--orange)"/></svg>Adults: 2</span>
      <span><svg class="ic" viewBox="0 0 34 34"><circle cx="17" cy="17" r="15" fill="none" stroke="var(--orange)" stroke-width="2.5"/><circle cx="17" cy="14" r="3" fill="var(--orange)"/><path d="M12 23c1-3 3-5 5-5s4 2 5 5" fill="var(--orange)"/></svg>Kids: 1</span>
    </div>
  </div>

  <h2 class="section-bar" style="top:1404px">RESERVATION DETAIL</h2>
  <div class="art res-art" style="top:1488px;height:272px" role="img" aria-label="Illustration of a guest checking a booking on a phone beside a clock"></div>
  <div class="res-item" style="top:1516px">Access (door code):<strong>01234 567890</strong></div>
  <div class="res-item" style="top:1650px">Check-in:<strong>Fri, Dec 25</strong></div>
  <div class="res-item" style="top:1768px">Checkout:<strong>Sun, Dec 27</strong></div>

  <div class="block amenities">
    <div class="amenity">
      <svg viewBox="0 0 92 92"><path d="M16 52l8-20c1-3 3-4 6-4h32c3 0 5 1 6 4l8 20v16H16z" fill="none" stroke="var(--ink)" stroke-width="5" stroke-linejoin="round"/><path d="M22 52h48" stroke="var(--ink)" stroke-width="5"/><circle cx="28" cy="60" r="3.5" fill="var(--ink)"/><circle cx="64" cy="60" r="3.5" fill="var(--ink)"/><rect x="20" y="68" width="10" height="8" fill="var(--ink)"/><rect x="62" y="68" width="10" height="8" fill="var(--ink)"/></svg>
      <p>Parking</p>
    </div>
    <div class="amenity">
      <svg viewBox="0 0 92 92"><g fill="none" stroke="var(--ink)" stroke-width="5" stroke-linecap="round"><path d="M12 38a48 48 0 0 1 68 0"/><path d="M22 49a34 34 0 0 1 48 0"/><path d="M32 60a20 20 0 0 1 28 0"/></g><circle cx="46" cy="70" r="5" fill="var(--ink)"/></svg>
      <p>Wifi</p>
    </div>
    <div class="amenity">
      <svg viewBox="0 0 92 92"><rect x="18" y="18" width="56" height="50" rx="4" fill="var(--mint-soft)" stroke="var(--ink)" stroke-width="4"/><rect x="26" y="28" width="16" height="10" rx="3" fill="none" stroke="var(--ink)" stroke-width="3"/><rect x="50" y="28" width="16" height="10" rx="3" fill="none" stroke="var(--ink)" stroke-width="3"/><path d="M18 46h56M18 56h56" stroke="var(--ink)" stroke-width="3"/><path d="M22 68v8M70 68v8" stroke="var(--ink)" stroke-width="4"/></svg>
      <p>House Rules</p>
    </div>
  </div>

  <div class="block property-band"></div>
  <h2 class="block property-title">PROPERTY DETAILS</h2>
  <div class="property-photo" role="img" aria-label="Property image placeholder: bright bedroom with a made bed and patterned rug"></div>
  <p class="block property-name">Harbor Loft Residences 5</p>
  <p class="block property-meta">4 BR / 4 BA / 12 PPL - Nashville, TN</p>

  <div class="block actions">
    <span class="btn btn-modify">MODIFY</span>
    <span class="btn btn-cancel">CANCLE</span>
  </div>

  <section class="block policy">
    <h2>POLICY DETAILS</h2>
    <p>This Privacy Policy describes Our policies and procedures on the collection, use and disclosure of Your information when You use the Service and tells You about Your privacy rights and how the law protects You.</p>
    <p>We use Your Personal data to provide and improve the Service. By using the Service, You agree to the collection and use of information in accordance with this Privacy Policy.</p>
    <span class="btn-read">READ MORE</span>
  </section>

  <section class="block help">
    <div class="help-info">
      <h2>GETTING HELP</h2>
      <div class="help-rule"></div>
      <div class="detail-row"><svg class="ic" viewBox="0 0 34 34"><circle cx="17" cy="17" r="15" fill="var(--orange)"/><path d="M12 10l3 0 1 4-2 1c1 2 2 3 4 4l1-2 4 1 0 3c-6 0-11-5-11-11z" fill="#fff"/></svg>555-014-2290</div>
      <div class="detail-row"><svg class="ic" viewBox="0 0 34 34"><circle cx="17" cy="17" r="15" fill="var(--orange)"/><rect x="10" y="12" width="14" height="10" fill="none" stroke="#fff" stroke-width="2"/><path d="M10 12l7 6 7-6" fill="none" stroke="#fff" stroke-width="2"/></svg>dana@inboxly.com</div>
      <div class="detail-row"><svg class="ic" viewBox="0 0 34 34"><circle cx="17" cy="17" r="15" fill="var(--orange)"/><circle cx="17" cy="17" r="8" fill="none" stroke="#fff" stroke-width="2"/><path d="M17 12v5l3 3" fill="none" stroke="#fff" stroke-width="2"/></svg>10am to 8pm</div>
    </div>
    <div class="emergency">
      <div class="emergency-art" role="img" aria-label="Illustration of a support agent with headset at a computer"></div>
      <p>Emergency Contact</p>
      <strong>555-014-2290</strong>
    </div>
  </section>

  <section class="block services">
    <h2>ADDITIONAL SERVICES</h2>
    <div class="services-rule"></div>
    <p>3 placeholders split into thirds 100% width at the bottom</p>
  </section>

  <footer class="block footer">
    <span>@loftquelle</span>
    <span class="social" aria-label="Social link"></span>
    <span class="social" aria-label="Social link"></span>
    <span class="social" aria-label="Social link"></span>
  </footer>
</main>
</body>
</html>
```